TOBREL Business Card Design

We need a business card design for a current Plastering company now moving to building and constructing new homes.
We have been in the Plastering(rendering) business for 15yrs and have made a good name with our customers for our Top Quality of work that we provide.
We would like TOBREL to be the main attraction with an image of architectural roof tops or house design within it. Blue Yellow and Black are colours we like but are willing to see other ideas.
We would like the design to be modern and communicate quality and experience.
Industry/Entity Type
Building
Contact Information for Business Card
TOBREL Building and Plastering
PO BOX 73519 Casuarina Darwin NT 0812
PH/Fax: 08 83170925 Email: tobrel@wavemail.example
Glen: 0419372654 Ruth:0408631597
ABN:57 208 931 446

```html
<!DOCTYPE html>
<html lang="en">
<head>
<meta charset="utf-8">
<title>TOBREL Building and Plastering – Business Cards</title>
<link rel="stylesheet" href="https://fonts.googleapis.com/css2?family=Open+Sans:wght@400;600;700;800&display=swap">
<style>
  :root {
    --navy-deep: #1e2d4a;
    --navy: #1e3560;
    --yellow: #ffcc00;
    --white: #ffffff;
    --label-grey: #444a55;
    --page: #ffffff;
    --shadow: 0 10px 22px rgba(0, 0, 0, 0.16), 0 2px 6px rgba(0, 0, 0, 0.08);
  }
  * { box-sizing: border-box; margin: 0; padding: 0; }
  html, body {
    width: 1200px; height: 840px; overflow: hidden;
    background: var(--page);
    font-family: "Open Sans", Arial, sans-serif;
  }
  .sheet { position: relative; width: 1200px; height: 840px; }

  .card {
    position: absolute; width: 486px; height: 304px;
    border-radius: 22px; overflow: hidden;
    box-shadow: var(--shadow);
  }
  .card--front-dark { left: 66px; top: 98px; background: var(--navy-deep); }
  .card--front-light { left: 645px; top: 96px; background: var(--navy); }
  .card--back-a { left: 60px; top: 472px; --panel: var(--navy-deep); }
  .card--back-b { left: 640px; top: 470px; --panel: var(--navy); }

  /* Wordmark */
  .wordmark {
    position: absolute; left: 0; right: 0; text-align: center;
    font-weight: 800; line-height: 1;
  }
  .wordmark__name { display: block; letter-spacing: 1px; }
  .wordmark__line { display: block; letter-spacing: 0.5px; }

  .card--front-dark .wordmark { top: 140px; color: var(--yellow); }
  .card--front-dark .wordmark__name { font-size: 46px; }
  .card--front-dark .wordmark__line { font-size: 17px; margin-top: 12px; }

  .gable { position: absolute; inset: 0; }
  .card--front-light .wordmark { top: 166px; color: var(--navy); }
  .card--front-light .wordmark__name { font-size: 54px; }
  .card--front-light .wordmark__line { font-size: 20px; margin-top: 16px; }

  /* Back */
  .contact-panel {
    position: absolute; left: 0; top: 0; width: 100%; height: 148px;
    background: var(--panel);
    border-bottom: 6px solid var(--yellow);
  }
  .contact-list { position: absolute; left: 62px; top: 28px; list-style: none; }
  .contact-list li {
    display: flex; align-items: center; gap: 10px;
    height: 25.5px; color: var(--white);
    font-size: 15px; font-weight: 700;
  }
  .contact-list svg { width: 18px; height: 14px; flex: none; }
  .abn {
    position: absolute; right: 78px; top: 118px;
    color: var(--white); font-size: 15px; font-weight: 700;
  }
  .people { position: absolute; left: 66px; top: 168px; }
  .person { margin-bottom: 20px; }
  .person__name { font-size: 16px; color: var(--label-grey); line-height: 22px; }
  .person__phone {
    display: flex; align-items: center; gap: 8px;
    font-size: 16px; font-weight: 700; color: var(--navy);
  }
  .person__phone svg { width: 11px; height: 16px; }

  .card--back-a .wordmark,
  .card--back-b .wordmark { left: 270px; right: 26px; top: 220px; color: var(--navy); }
  .card--back-a .wordmark__name,
  .card--back-b .wordmark__name { font-size: 30px; }
  .card--back-a .wordmark__line,
  .card--back-b .wordmark__line { font-size: 11.5px; margin-top: 8px; }
  .back-body { position: absolute; inset: 0; background: var(--white); }
</style>
</head>
<body>
<main class="sheet">

  <section class="card card--front-dark" aria-label="Card front, dark">
    <div class="wordmark">
      <span class="wordmark__name">TOBREL</span>
      <span class="wordmark__line">BUILDING &amp; PLASTERING</span>
    </div>
  </section>

  <section class="card card--front-light" aria-label="Card front, light">
    <svg class="gable" viewBox="0 0 486 304" preserveAspectRatio="none" aria-hidden="true">
      <polygon points="0,160 243,44 486,160 486,304 0,304" fill="var(--white)"/>
      <rect x="0" y="281" width="486" height="23" fill="var(--yellow)"/>
    </svg>
    <div class="wordmark">
      <span class="wordmark__name">TOBREL</span>
      <span class="wordmark__line">BUILDING &amp; PLASTERING</span>
    </div>
  </section>

  <section class="card card--back-a" aria-label="Card back">
    <div class="back-body"></div>
    <div class="contact-panel">
      <ul class="contact-list">
        <li><svg viewBox="0 0 18 14" aria-hidden="true"><path d="M1 7 Q9 -1 17 7 Q9 15 1 7Z" fill="none" stroke="#fff" stroke-width="1.6"/><circle cx="9" cy="7" r="2.6" fill="#fff"/></svg>PO BOX 73519 Casuarina Darwin NT 0812</li>
        <li><svg viewBox="0 0 18 14" aria-hidden="true"><rect x="4" y="1" width="10" height="4" fill="none" stroke="#fff" stroke-width="1.4"/><rect x="1" y="5" width="16" height="6" rx="1" fill="#fff"/><rect x="4" y="9" width="10" height="4" fill="#fff" stroke="var(--panel)" stroke-width="1"/></svg>PH/Fax: 08 83170925</li>
        <li><svg viewBox="0 0 18 14" aria-hidden="true"><rect x="1" y="2" width="16" height="10" fill="none" stroke="#fff" stroke-width="1.4"/><path d="M1 2 L9 8 L17 2" fill="none" stroke="#fff" stroke-width="1.4"/></svg>tobrel@wavemail.example</li>
      </ul>
      <p class="abn">ABN:57 208 931 446</p>
    </div>
    <div class="people">
      <div class="person">
        <p class="person__name">Glen:</p>
        <p class="person__phone"><svg viewBox="0 0 11 16" aria-hidden="true"><rect x="1" y="1" width="9" height="14" rx="1.5" fill="none" stroke="var(--navy)" stroke-width="1.4"/><line x1="4" y1="12.5" x2="7" y2="12.5" stroke="var(--navy)" stroke-width="1.2"/></svg>0419372654</p>
      </div>
      <div class="person">
        <p class="person__name">Ruth:</p>
        <p class="person__phone"><svg viewBox="0 0 11 16" aria-hidden="true"><rect x="1" y="1" width="9" height="14" rx="1.5" fill="none" stroke="var(--navy)" stroke-width="1.4"/><line x1="4" y1="12.5" x2="7" y2="12.5" stroke="var(--navy)" stroke-width="1.2"/></svg>0408631597</p>
      </div>
    </div>
    <div class="wordmark">
      <span class="wordmark__name">TOBREL</span>
      <span class="wordmark__line">BUILDING &amp; PLASTERING</span>
    </div>
  </section>

  <section class="card card--back-b" aria-label="Card back, alternate">
    <div class="back-body"></div>
    <div class="contact-panel">
      <ul class="contact-list">
        <li><svg viewBox="0 0 18 14" aria-hidden="true"><path d="M1 7 Q9 -1 17 7 Q9 15 1 7Z" fill="none" stroke="#fff" stroke-width="1.6"/><circle cx="9" cy="7" r="2.6" fill="#fff"/></svg>PO BOX 73519 Casuarina Darwin NT 0812</li>
        <li><svg viewBox="0 0 18 14" aria-hidden="true"><rect x="4" y="1" width="10" height="4" fill="none" stroke="#fff" stroke-width="1.4"/><rect x="1" y="5" width="16" height="6" rx="1" fill="#fff"/><rect x="4" y="9" width="10" height="4" fill="#fff" stroke="var(--panel)" stroke-width="1"/></svg>PH/Fax: 08 83170925</li>
        <li><svg viewBox="0 0 18 14" aria-hidden="true"><rect x="1" y="2" width="16" height="10" fill="none" stroke="#fff" stroke-width="1.4"/><path d="M1 2 L9 8 L17 2" fill="none" stroke="#fff" stroke-width="1.4"/></svg>tobrel@wavemail.example</li>
      </ul>
      <p class="abn">ABN:57 208 931 446</p>
    </div>
    <div class="people">
      <div class="person">
        <p class="person__name">Glen:</p>
        <p class="person__phone"><svg viewBox="0 0 11 16" aria-hidden="true"><rect x="1" y="1" width="9" height="14" rx="1.5" fill="none" stroke="var(--navy)" stroke-width="1.4"/><line x1="4" y1="12.5" x2="7" y2="12.5" stroke="var(--navy)" stroke-width="1.2"/></svg>0419372654</p>
      </div>
      <div class="person">
        <p class="person__name">Ruth:</p>
        <p class="person__phone"><svg viewBox="0 0 11 16" aria-hidden="true"><rect x="1" y="1" width="9" height="14" rx="1.5" fill="none" stroke="var(--navy)" stroke-width="1.4"/><line x1="4" y1="12.5" x2="7" y2="12.5" stroke="var(--navy)" stroke-width="1.2"/></svg>0408631597</p>
      </div>
    </div>
    <div class="wordmark">
      <span class="wordmark__name">TOBREL</span>
      <span class="wordmark__line">BUILDING &amp; PLASTERING</span>
    </div>
  </section>

</main>
</body>
</html>
```